Banner Design for Holistic Clinic

We need a banner to be designed for a Holistic Clinic which treats patient using IV Nutrition therapy, IV Vitamin C therapy, Chelation therapy, Homoepathy , Accupuncture, Ayurveda. Our website is www.verdantcarehub.in

We need the banner to show case all our services. IV Nutrition therapy, IV Vitamin C therapy, Chelation therapy, Homoepathy , Accupuncture, Ayurveda with special emphasis on IV Therapies. This will be in the front of the web page and will be used for leaflets and flex material.Ideally

I like the concept of IV infsuion bags, fruits etc. I have attached some of the pic which i liked. Please see the attachment "banner clinic july 13" But feel free to change it and bring in something better that will showcase all our services together

Target Market(s)

30 plus Adults

Industry/Entity Type

Health And Wellness

Font styles to use
Serif

Colors
acd036
f37122
33a6d7

Requirements
Must have
• Some samples are given below. It got to be colourful, yet pleasing.

```html
<!DOCTYPE html>
<html lang="en">
<head>
<meta charset="utf-8">
<title>Verdant Care Hub – Services Banner</title>
<link href="https://fonts.googleapis.com/css2?family=Arvo:wght@700&display=swap" rel="stylesheet">
<style>
  :root{
    --sky-grey:#b9bec4;
    --sky-grey-light:#dfe2e5;
    --swoosh-blue:#1a6fb0;
    --swoosh-blue-deep:#0f5d9c;
    --paper:#ffffff;
    --paper-grey:#eceef0;
    --bag-white:#fbfbfb;
    --bag-edge:#d9dcdf;
    --port-clear:#d2d5d8;
    --port-blue:#2aa7d9;
    --label-green:#1e9b3f;
    --headline:#3a3a3c;
  }
  *{box-sizing:border-box;margin:0;padding:0}
  html,body{width:1200px;height:607px;overflow:hidden;background:var(--paper)}
  .banner{position:relative;width:1200px;height:607px;overflow:hidden;font-family:"Arvo",serif}
  .backdrop{position:absolute;inset:0}

  .iv-bag{position:absolute;top:60px;width:156px;height:372px;filter:drop-shadow(3px 5px 5px rgba(0,0,0,.28))}
  .iv-bag svg.bag-shell{position:absolute;inset:0}
  .brand-name{position:absolute;top:34px;left:10px;right:10px;text-align:center;font-family:"Arvo",serif;font-weight:700;font-size:10px;line-height:1;color:var(--label-green);white-space:nowrap}

  .therapy-visual{position:absolute;top:56px;left:12px;width:132px;height:196px;border-radius:26px}
  .visual-chelation{background:radial-gradient(ellipse at 50% 55%,#c9283a 0%,#e27a86 30%,#f6cfd4 60%,var(--bag-white) 82%)}
  .visual-vitc{background:radial-gradient(ellipse at 50% 50%,#f49b1c 0%,#f8b445 45%,#fbd79a 70%,var(--bag-white) 90%)}
  .visual-nutrition{background:radial-gradient(ellipse at 50% 50%,#e8c640 0%,#b8cf6e 35%,#d9473c 60%,#f1d9d0 78%,var(--bag-white) 92%)}
  .visual-acupuncture{background:radial-gradient(ellipse at 50% 55%,#d6a98a 0%,#e6c4ab 45%,#f3e4d8 70%,var(--bag-white) 88%)}
  .visual-homoeopathy{background:radial-gradient(ellipse at 50% 50%,#ffffff 0%,#dfe6ee 35%,#9fb2c7 60%,#e7ecf1 80%,var(--bag-white) 92%)}
  .visual-ayurveda{background:radial-gradient(ellipse at 50% 45%,#5b3a22 0%,#9a6a3d 30%,#d3b389 58%,#f3ebdf 80%,var(--bag-white) 92%)}

  .therapy-label{position:absolute;top:256px;left:8px;right:8px;height:48px;display:flex;align-items:center;justify-content:center;text-align:center;font-family:"Arvo",serif;font-weight:700;font-size:15px;line-height:1.05;color:var(--label-green)}

  .headline{position:absolute;left:0;right:0;top:478px;text-align:center;font-family:"Arvo",serif;font-weight:700;font-size:78px;letter-spacing:-1px;color:var(--headline);line-height:1}
</style>
</head>
<body>
<main class="banner">
  <svg class="backdrop" width="1200" height="607" viewBox="0 0 1200 607" aria-hidden="true">
    <defs>
      <linearGradient id="sky" x1="0" y1="0" x2="0" y2="1">
        <stop offset="0" stop-color="#dfe2e5"/>
        <stop offset="1" stop-color="#b9bec4"/>
      </linearGradient>
    </defs>
    <rect width="1200" height="607" fill="url(#sky)"/>
    <path d="M0,190 C300,150 600,140 860,190 C1000,220 1120,200 1200,170 L1200,607 L0,607 Z" fill="var(--swoosh-blue)"/>
    <path d="M0,240 C260,200 560,210 820,260 C960,290 1080,300 1200,330 L1200,607 L0,607 Z" fill="var(--paper)"/>
    <path d="M1200,330 C1080,300 960,300 900,310 C1000,330 1120,360 1200,390 Z" fill="var(--swoosh-blue-deep)"/>
    <path d="M1200,390 C1000,360 760,380 560,430 C760,400 1000,410 1200,460 Z" fill="var(--paper-grey)"/>
    <path d="M0,520 C240,470 520,470 780,530 C520,500 260,510 0,560 Z" fill="var(--paper-grey)"/>
  </svg>

  <svg width="0" height="0" style="position:absolute" aria-hidden="true">
    <symbol id="bag-body" viewBox="0 0 156 372">
      <path d="M14,2 H142 Q154,2 152,16 Q146,60 146,110 V230 Q146,272 153,298 Q156,318 140,320 H16 Q0,318 3,298 Q10,272 10,230 V110 Q10,60 4,16 Q2,2 14,2 Z" fill="var(--bag-white)" stroke="var(--bag-edge)" stroke-width="1"/>
      <rect x="56" y="12" width="44" height="16" rx="8" fill="var(--sky-grey)"/>
      <path d="M40,320 L48,336 H74 L80,320 Z" fill="#eceef0" stroke="var(--bag-edge)"/>
      <path d="M82,320 L88,336 H112 L118,320 Z" fill="#eceef0" stroke="var(--bag-edge)"/>
      <rect x="57" y="336" width="8" height="30" fill="var(--port-clear)"/>
      <rect x="55" y="358" width="12" height="12" rx="2" fill="#c4c7ca"/>
      <rect x="97" y="336" width="8" height="12" fill="var(--port-clear)"/>
      <rect x="95" y="346" width="12" height="22" rx="3" fill="var(--port-blue)"/>
    </symbol>
  </svg>

  <section class="iv-bag" style="left:84px">
    <svg class="bag-shell" viewBox="0 0 156 372" aria-hidden="true"><use href="#bag-body"/></svg>
    <p class="brand-name">Verdant Care Hub</p>
    <div class="therapy-visual visual-chelation" role="img" aria-label="Illustration of a human heart with blood vessels"></div>
    <h2 class="therapy-label">Chelation<br>Therapy</h2>
  </section>

  <section class="iv-bag" style="left:260px">
    <svg class="bag-shell" viewBox="0 0 156 372" aria-hidden="true"><use href="#bag-body"/></svg>
    <p class="brand-name">Verdant Care Hub</p>
    <div class="therapy-visual visual-vitc" role="img" aria-label="Photo of sliced oranges"></div>
    <h2 class="therapy-label">IV Vitamin<br>C Therapy</h2>
  </section>

  <section class="iv-bag" style="left:436px">
    <svg class="bag-shell" viewBox="0 0 156 372" aria-hidden="true"><use href="#bag-body"/></svg>
    <p class="brand-name">Verdant Care Hub</p>
    <div class="therapy-visual visual-nutrition" role="img" aria-label="Photo of fresh fruits: grapes, lemon, apple and melon"></div>
    <h2 class="therapy-label">IV Nutrition<br>Therapy</h2>
  </section>

  <section class="iv-bag" style="left:612px">
    <svg class="bag-shell" viewBox="0 0 156 372" aria-hidden="true"><use href="#bag-body"/></svg>
    <p class="brand-name">Verdant Care Hub</p>
    <div class="therapy-visual visual-acupuncture" role="img" aria-label="Photo of acupuncture needles being placed on a patient's back"></div>
    <h2 class="therapy-label">Accupuncture</h2>
  </section>

  <section class="iv-bag" style="left:788px">
    <svg class="bag-shell" viewBox="0 0 156 372" aria-hidden="true"><use href="#bag-body"/></svg>
    <p class="brand-name">Verdant Care Hub</p>
    <div class="therapy-visual visual-homoeopathy" role="img" aria-label="Photo of white homoeopathic pills spilling from a bottle"></div>
    <h2 class="therapy-label">Homoepathy</h2>
  </section>

  <section class="iv-bag" style="left:964px">
    <svg class="bag-shell" viewBox="0 0 156 372" aria-hidden="true"><use href="#bag-body"/></svg>
    <p class="brand-name">Verdant Care Hub</p>
    <div class="therapy-visual visual-ayurveda" role="img" aria-label="Photo of Ayurvedic herbs, spices and a mortar with paste"></div>
    <h2 class="therapy-label">Ayurveda</h2>
  </section>

  <h1 class="headline">Your Text Here</h1>
</main>
</body>
</html>
```